Global Voltara Energy Technology Company needs initial Web Design

We need a web design for new Voltara Energy Technology company. The company has developed innovative technology and needs a website to reflect this branding. Whilst this assignment will represent the initial site we are seeking an ongoing relationship to allow the website to be developed as the business develops. The logo design and initial artwork has been done and needs to incorporated in the design.

Target Market(s)

Business decision makers and power generation companies
Initially two target markets
1. Commercial users like construction companies or industrial businesses like mining that currently utilize Diesel generators to create power
2. Electrical power suppliers that currently use diesel generators in regional and remote to supply remote communities like outback Australia or pacific islands like Fuji etc
The purpose initially is to showcase/ educate customers about the product but we ideally would like to capture email addressees as part of this process.

The product information has been limited at this stage as we are currently finalizing IP registrations.

The main competitors are
1 Solar energy products but these only generate power when the sun is shinning and needs to be stored which battery technology is expensive and will only last up to 3 days at most
2 Wind energy would the same as as solar
3 Diesel generators run continually but are expensive to operate. Our product would be approximately 1/2 the operating cost of this energy source. There is no reliance on fuel sources so the user doesn't need to store fuel, worry about running out or fluctuations in fuel pricing. Diesel generators are very noisy and not environmentally friendly.

Industry/Entity Type

Solar Energy

Coding

Coded - Design and coding required

Number of Pages Required

4 page

Font styles to use
Sans Serif

Colors
acd036
33a6d7
ffffff

Requirements
Must have
• This version is intended as an initial basic 4 page website only.
• It should be built on the basis that it can be expanded after the products are formally launched into the market. A separate assignment will be allocated to the successful initial website designer to create a more elaborate site with a budget to match. The format and content for the initial site is outlined in the attached word document (File 1) The remaining files contain the logo and existing artwork and associated colours. The site should have the ability to view on smart phones and tablets.

```html
<!DOCTYPE html>
<html lang="en">
<head>
<meta charset="utf-8">
<title>Voltara Energy</title>
<link href="https://fonts.googleapis.com/css2?family=Ubuntu:wght@400;500&family=Open+Sans:wght@400;600&display=swap" rel="stylesheet">
<style>
:root{
  --green:#1e9e1e;
  --green-btn:#0fa80f;
  --lime:#acd036;
  --blue:#33a6d7;
  --ink:#222;
  --text:#444;
  --grey-bg:#f1f1f1;
  --field:#ececec;
  --footer:#232323;
  --footer-bottom:#141414;
  --white:#fff;
}
*{margin:0;padding:0;box-sizing:border-box}
html,body{width:1200px;height:2273px;overflow:hidden;background:var(--white)}
body{position:relative;font-family:"Open Sans",Arial,sans-serif;color:var(--text)}
.abs{position:absolute}
h1,h2,h3,.nav-title,.brand{font-family:"Ubuntu",Arial,sans-serif;font-weight:400}

/* header */
.topline{left:0;top:0;width:1200px;height:4px;background:var(--green)}
.header{left:0;top:4px;width:1200px;height:114px;background:var(--white);box-shadow:0 6px 10px rgba(0,0,0,.18);z-index:2}
.brand{display:flex;align-items:center;gap:12px;color:var(--lime);font-size:28px;font-weight:500;letter-spacing:1px}
.brand-dot{width:62px;height:62px;border-radius:50%;background:var(--blue)}
.header .brand{left:98px;top:26px}
.nav{left:440px;top:38px;display:flex}
.nav-item{padding-left:34px;border-left:1px solid #e6e6e6;height:52px}
.nav-item:first-child{border-left:none;padding-left:24px}
.nav-title{font-size:14px;color:var(--ink);letter-spacing:.3px}
.nav-sub{font-size:11px;color:var(--ink);margin-top:8px}
.nav-item.active .nav-title{color:var(--green)}

/* hero */
.hero{left:0;top:118px;width:1200px;height:522px;overflow:hidden}
.hero-backdrop{left:0;top:0;width:1200px;height:522px;background:linear-gradient(180deg,#8fd2ef 0%,#cdebf7 100%)}
.hero h1{left:152px;top:84px;font-size:40px;color:#333}
.hero h2{left:154px;top:138px;font-size:26px;color:var(--green)}
.hero-list{list-style:none;font-size:15px;color:#222}
.hero-list li{height:27.5px;display:flex;align-items:center;gap:16px}
.tick{width:12px;height:12px}
.product-photo{left:700px;top:124px;width:345px;height:350px;border-radius:4px;background:linear-gradient(135deg,#f4f6f8,#c9d3dc 55%,#3ea4d6 100%)}
.arrow-btn{width:34px;height:34px;border-radius:50%;background:#4a4a4a;top:450px;display:flex;align-items:center;justify-content:center}

/* people */
.section-title{width:1200px;text-align:center;font-family:"Ubuntu",Arial,sans-serif;font-weight:500;font-size:34px;color:var(--ink)}
.person{width:300px;text-align:center}
.person-photo{width:176px;height:176px;border-radius:50%;margin:0 auto;border:3px solid #eee;background:linear-gradient(180deg,#c9ccd0,#5a5f66)}
.person-shadow{width:140px;height:8px;margin:14px auto 0;border-radius:50%;background:radial-gradient(ellipse,rgba(0,0,0,.12),transparent 70%)}
.person-name{font-family:"Ubuntu",Arial,sans-serif;font-size:18px;color:#333;margin-top:8px}
.person-role{font-size:10px;color:#333;margin-top:6px}
.person-contact{font-size:11px;color:#444;line-height:22px;margin-top:14px}

/* welcome */
.welcome{left:0;top:1148px;width:1200px;height:409px;background:radial-gradient(circle at 50% 50%,#fafafa,var(--grey-bg))}
.video{left:98px;top:69px;width:405px;height:290px;background:var(--white);border:1px solid #ddd;padding:8px}
.video-screen{width:100%;height:244px;background:linear-gradient(180deg,#8fd2ef,#d6eff9)}
.video-play{right:20px;top:24px;width:36px;height:36px;border-radius:50%;background:#666;display:flex;align-items:center;justify-content:center}
.video-bar{height:22px;display:flex;align-items:center;gap:10px;font-size:8px;color:#333;padding:0 6px}
.track{height:3px;background:#555;flex:1;position:relative}
.track span{position:absolute;left:0;top:0;height:3px;width:45%;background:#e0453a}
.welcome h2{left:545px;top:62px;font-size:30px;color:#111;line-height:36px}
.welcome h2 span{color:var(--green);display:block;margin-top:4px}
.welcome-copy{left:545px;top:150px;width:540px;font-size:11.5px;line-height:20.5px;color:#444}
.welcome-copy p+p{margin-top:14px}
.read-more{left:545px;top:344px;font-size:13px;color:#333;display:flex;align-items:center;gap:8px}

/* subscribe & news */
.subscribe{left:98px;top:1623px;width:436px;height:316px;border:1px solid #ddd}
.subscribe h3{left:80px;top:16px;font-size:21px;color:#222;line-height:25px;text-transform:uppercase}
.subscribe .lead{left:26px;top:84px;width:380px;font-size:14px;line-height:20px;color:#333}
.field{background:var(--field);font-size:12px;color:#444;padding-left:16px;display:flex;align-items:center;height:40px}
.btn{background:var(--green-btn);color:var(--white);font-size:14px;display:flex;align-items:center;justify-content:center;height:40px}
.subscribe .brand{left:26px;top:250px;font-size:21px;gap:10px}
.subscribe .brand-dot{width:46px;height:46px}
.news-title{left:573px;top:1618px;font-family:"Ubuntu",Arial,sans-serif;font-size:22px;color:#333}
.news-img{width:172px;height:118px}
.news-h{font-size:14px;color:var(--green)}
.news-time{font-size:12px;color:#333;display:flex;align-items:center;gap:6px}
.news-text{width:335px;font-size:11.5px;line-height:21px;color:#444}

/* footer */
.footer{left:0;top:2007px;width:1200px;height:206px;background:var(--footer);color:var(--white)}
.footer h4{font-family:"Ubuntu",Arial,sans-serif;font-weight:500;font-size:17px}
.footer .small{font-size:12px;line-height:21px}
.contact-row{display:flex;align-items:center;gap:16px}
.social{display:flex;gap:20px}
.social span{width:56px;height:56px;border:2.5px solid var(--white);border-radius:50%}
.legal{left:0;top:2213px;width:1200px;height:60px;background:var(--footer-bottom);color:var(--white);font-size:11px;display:flex;align-items:center;justify-content:center}
</style>
</head>
<body>

<div class="abs topline"></div>
<header class="abs header">
  <div class="abs brand"><span class="brand-dot"></span>VOLTARA ENERGY</div>
  <nav class="abs nav">
    <div class="nav-item active" style="width:109px"><div class="nav-title">HOME</div><div class="nav-sub">Start page</div></div>
    <div class="nav-item" style="width:144px"><div class="nav-title">ABOUT US</div><div class="nav-sub">Who we are</div></div>
    <div class="nav-item" style="width:156px"><div class="nav-title">OUR PRODUCTS</div><div class="nav-sub">What we offer</div></div>
    <div class="nav-item" style="width:151px"><div class="nav-title">OUR PEOPLE</div><div class="nav-sub">Our works</div></div>
    <div class="nav-item"><div class="nav-title">CONTACT</div><div class="nav-sub">Get in touch</div></div>
  </nav>
</header>

<section class="abs hero">
  <div class="abs hero-backdrop" role="img" aria-label="Backdrop photo: blue sky over a grass field and wooden deck"></div>
  <h1 class="abs">Voltara Energy</h1>
  <h2 class="abs">The Ultimate Power</h2>
  <ul class="abs hero-list" style="left:158px;top:183px">
    <li><svg class="tick" viewBox="0 0 12 12"><path d="M1 6l3.5 3.5L11 2" fill="none" stroke="#1e9e1e" stroke-width="2.5"/></svg>24 hour a day power</li>
    <li><svg class="tick" viewBox="0 0 12 12"><path d="M1 6l3.5 3.5L11 2" fill="none" stroke="#1e9e1e" stroke-width="2.5"/></svg>No fuel sources</li>
    <li><svg class="tick" viewBox="0 0 12 12"><path d="M1 6l3.5 3.5L11 2" fill="none" stroke="#1e9e1e" stroke-width="2.5"/></svg>Environmentally friendly</li>
    <li><svg class="tick" viewBox="0 0 12 12"><path d="M1 6l3.5 3.5L11 2" fill="none" stroke="#1e9e1e" stroke-width="2.5"/></svg>Scalable and relocatable</li>
  </ul>
  <ul class="abs hero-list" style="left:390px;top:183px">
    <li><svg class="tick" viewBox="0 0 12 12"><path d="M1 6l3.5 3.5L11 2" fill="none" stroke="#1e9e1e" stroke-width="2.5"/></svg>Quick and easy installation</li>
    <li><svg class="tick" viewBox="0 0 12 12"><path d="M1 6l3.5 3.5L11 2" fill="none" stroke="#1e9e1e" stroke-width="2.5"/></svg>Full maintenance support</li>
    <li><svg class="tick" viewBox="0 0 12 12"><path d="M1 6l3.5 3.5L11 2" fill="none" stroke="#1e9e1e" stroke-width="2.5"/></svg>24 hour monitoring</li>
    <li><svg class="tick" viewBox="0 0 12 12"><path d="M1 6l3.5 3.5L11 2" fill="none" stroke="#1e9e1e" stroke-width="2.5"/></svg>20 year &nbsp;warranty</li>
  </ul>
  <div class="abs product-photo" role="img" aria-label="Photo of the white and blue generator unit"></div>
  <div class="abs arrow-btn" style="left:154px"><svg width="12" height="14" viewBox="0 0 12 14"><path d="M9 1L3 7l6 6" fill="none" stroke="#fff" stroke-width="2.5"/></svg></div>
  <div class="abs arrow-btn" style="left:197px"><svg width="12" height="14" viewBox="0 0 12 14"><path d="M3 1l6 6-6 6" fill="none" stroke="#fff" stroke-width="2.5"/></svg></div>
</section>

<h2 class="abs section-title" style="left:0;top:692px">OUR PEOPLE</h2>

<div class="abs person" style="left:64px;top:779px">
  <div class="person-photo" role="img" aria-label="Portrait of the global engineering director"></div>
  <div class="person-shadow"></div>
  <div class="person-name">Graham Pellow</div>
  <div class="person-role">Global Engineering Director</div>
  <div class="person-contact">Phone +61 400 123 456<br>graham.pellow@voltaraenergy.com</div>
</div>
<div class="abs person" style="left:312px;top:779px">
  <div class="person-photo" role="img" aria-label="Portrait of the managing director"></div>
  <div class="person-shadow"></div>
  <div class="person-name">Marek Dolan</div>
  <div class="person-role">Managing Director</div>
  <div class="person-contact">Phone +61 400 123 456<br>marek.dolan@voltaraenergy.com</div>
</div>
<div class="abs person" style="left:579px;top:779px">
  <div class="person-photo" role="img" aria-label="Portrait of the chief financial officer"></div>
  <div class="person-shadow"></div>
  <div class="person-name">Simon Harwick</div>
  <div class="person-role">Chief Financial Officer</div>
  <div class="person-contact">Phone +61 400 123 456<br>simon.harwick@voltaraenergy.com</div>
</div>
<div class="abs person" style="left:835px;top:779px">
  <div class="person-photo" role="img" aria-label="Portrait of the quality director"></div>
  <div class="person-shadow"></div>
  <div class="person-name">Anan Sirichai</div>
  <div class="person-role">Quality Director</div>
  <div class="person-contact">Phone +61 400 123 456<br>anan.sirichai@voltaraenergy.com</div>
</div>

<section class="abs welcome">
  <div class="abs video">
    <div class="video-screen" role="img" aria-label="Video still: company emblem against sky and grass"></div>
    <div class="abs video-play"><svg width="14" height="16" viewBox="0 0 14 16"><path d="M2 1l11 7-11 7z" fill="#fff"/></svg></div>
    <div class="video-bar">
      <svg width="8" height="8" viewBox="0 0 8 8"><path d="M1 0l7 4-7 4z" fill="#333"/></svg>
      <span>10:00/05:03</span>
      <div class="track"><span></span></div>
      <svg width="12" height="10" viewBox="0 0 12 10"><path d="M0 3h3l4-3v10L3 7H0z" fill="#333"/></svg>
      <div class="track" style="flex:0 0 40px"><span style="width:100%"></span></div>
    </div>
  </div>
  <h2 class="abs">WELCOME TO<span>Voltara Energy</span></h2>
  <div class="abs welcome-copy">
    <p>Voltara Energy has developed patented electric power generation technology that revolutionises the way the world will think about power generation for generations to come. The advanced generator technology has been designed in a way that there are minimal energy losses. The generator, coupled with the intelligent mechanical and electronic multipliers, allows the system to produce very high input to output ratios resulting in ratios of 1 to 100 outputs.</p>
    <p>These transportable Units require no external fuel sources making them completely environmentally friendly. &nbsp;Low noise and no emissions enables these environmentally friendly units to be co-located within modern residential, industrial and commercial centres, minimising transmission loss.</p>
  </div>
  <div class="abs read-more">READ MORE <svg width="12" height="12" viewBox="0 0 12 12"><circle cx="6" cy="6" r="6" fill="#333"/><path d="M5 3l3 3-3 3" fill="none" stroke="#fff" stroke-width="1.6"/></svg></div>
</section>

<section class="abs subscribe">
  <svg class="abs" style="left:24px;top:16px" width="40" height="44" viewBox="0 0 40 44"><path d="M8 4h24v14H8z" fill="#1e9e1e"/><path d="M2 16h36v26H2z" fill="#1e9e1e"/><path d="M2 16l18 14 18-14" fill="none" stroke="#fff" stroke-width="2"/><path d="M13 9h14M13 13h14" stroke="#fff" stroke-width="2"/></svg>
  <h3 class="abs">Subscribe to<br>Insight</h3>
  <p class="abs lead">Lorem ipsum dolor sit amet, consectetur adipiscing elit, sed do eiusmod tempor incididunt ut labore</p>
  <div class="abs field" style="left:26px;top:138px;width:384px">Email Address</div>
  <div class="abs field" style="left:26px;top:191px;width:234px">Postcode</div>
  <div class="abs btn" style="left:272px;top:191px;width:138px">SUBSCRIBE</div>
  <div class="abs brand"><span class="brand-dot"></span>VOLTARA ENERGY</div>
</section>

<h3 class="abs news-title">News &amp; Updates</h3>
<div class="abs news-img" style="left:573px;top:1673px;background:linear-gradient(180deg,#9cc6e8,#5f7f99)" role="img" aria-label="Photo of glass office towers"></div>
<div class="abs news-h" style="left:768px;top:1670px">Nemo Enim Ipsam Voluptatem</div>
<div class="abs news-time" style="left:768px;top:1699px"><svg width="11" height="11" viewBox="0 0 12 12"><circle cx="6" cy="6" r="5" fill="none" stroke="#333" stroke-width="1.6"/><path d="M6 3v3h2.5" fill="none" stroke="#333" stroke-width="1.4"/></svg>19.00 pm - 21.00 pm</div>
<p class="abs news-text" style="left:768px;top:1725px">Lorem ipsum dolor sit amet, consectetur adipiscing elit, sed do eiusmod tempor incididunt ut labore et dolore magna aliqua. Ut enim ad minim veniam,</p>

<div class="abs news-img" style="left:573px;top:1826px;background:linear-gradient(180deg,#6fa3d8,#c9bd98)" role="img" aria-label="Photo of a row of suburban houses"></div>
<div class="abs news-h" style="left:768px;top:1822px">Nemo Enim Ipsam Voluptatem</div>
<div class="abs news-time" style="left:768px;top:1851px"><svg width="11" height="11" viewBox="0 0 12 12"><circle cx="6" cy="6" r="5" fill="none" stroke="#333" stroke-width="1.6"/><path d="M6 3v3h2.5" fill="none" stroke="#333" stroke-width="1.4"/></svg>19.00 pm - 21.00 pm</div>
<p class="abs news-text" style="left:768px;top:1877px">Lorem ipsum dolor sit amet, consectetur adipiscing elit, sed do eiusmod tempor incididunt ut labore et dolore magna aliqua. Ut enim ad minim veniam,</p>

<footer class="abs footer">
  <h4 class="abs" style="left:97px;top:42px">CONTACT US</h4>
  <p class="abs small" style="left:97px;top:71px">77 Moo 5 Rim Ping Road Saraphi District<br>Chiang Mai, THAILAND</p>
  <div class="abs contact-row" style="left:100px;top:118px;font-size:16px">
    <svg width="16" height="16" viewBox="0 0 16 16"><path d="M3 1l3 3-2 2c1 2 3 4 5 5l2-2 3 3-2 3C7 15 1 9 1 3z" fill="none" stroke="#fff" stroke-width="1.3"/></svg>+11-800-555-0142
  </div>
  <div class="abs contact-row small" style="left:100px;top:146px">
    <svg width="16" height="12" viewBox="0 0 16 12"><rect x="1" y="1" width="14" height="10" fill="none" stroke="#fff" stroke-width="1.3"/><path d="M1 1l7 6 7-6" fill="none" stroke="#fff" stroke-width="1.3"/></svg>info@voltaraenergy.com
  </div>
  <h4 class="abs" style="left:442px;top:42px">FOLLOW US</h4>
  <div class="abs social" style="left:442px;top:80px"><span></span><span></span><span></span><span></span></div>
  <h4 class="abs" style="left:809px;top:42px">OUR PRODUCTS</h4>
  <p class="abs small" style="left:809px;top:71px;width:300px;font-size:11.5px">Lorem ipsum dolor sit amet, consectetur adipiscing elit, sed do eiusmod tempor incididunt ut labore et dolore magna aliqua. Ut enim ad minim veniam, quis nostrud exercitation ullamco laboris nisi ut aliquip ex ea commodo consequat. Duis aute irure</p>
</footer>
<div class="abs legal">2015 &nbsp;All Rights Reserved. Voltara Energy</div>

</body>
</html>
```